Flyer for annual KESTREL SUMMIT 2020

I would like a church event flyer designed. The event is called "KESTREL SUMMIT 2020". I am looking for a professional, yet catchy design that uses our brand colors and logo creatively while communicating key information of the event effectively.

1. The logo is attached in two color formats. The designer has the choice to use them as he/she want.

2. The location of the event is: Harlow Community Center, 239 Fennimore Street, Portland, ME 04117

3. Time and date of event. The designer can organize and format the date and time as he/she pleases.
Thursday December 31st @ 6:30PM
Friday January 1st @ 6:30PM
Saturday 2nd @ 6:30PM
Sunday 3rd @ 4:30PM

4. The topic of the event is "In Fire and On Fire". The designer is free to use this phrase as he/she pleases to create a good composition.

5. Speaker: Prophet Marcus Olunde (2 pictures of the speaker to choose from are attached)

6. Contact information: contact@brightmeadowfold.org - Telephone number: 207 583 2914

7. I would also like the following three words on the flyer. These words describe the focus of the event: FIRE, REVIVAL, PROPHETIC

Target Market(s)

Young adults

Font styles to use
Sans Serif

Requirements
Must have
• Logo, speaker's picture
Should not have
• cross image, church image

```html
<!DOCTYPE html>
<html lang="en">
<head>
<meta charset="utf-8">
<title>Kestrel Summit 2020 – Flyer</title>
<link rel="stylesheet" href="https://fonts.googleapis.com/css2?family=Fira+Sans:ital,wght@0,400;0,600;0,700;1,500&display=swap">
<style>
  :root {
    --navy: #0f3a5f;
    --orange: #f49423;
    --ink: #262626;
    --paper: #f4f4f4;
    --white: #ffffff;
  }
  * { margin: 0; padding: 0; box-sizing: border-box; }
  html, body { width: 849px; height: 1200px; overflow: hidden; background: var(--paper); }
  body { font-family: "Fira Sans", Arial, sans-serif; color: var(--ink); }
  .flyer { position: relative; width: 849px; height: 1200px; overflow: hidden;
    background: linear-gradient(180deg, #dadada 0%, #ececec 45%, #ffffff 80%); }
  .flame-backdrop { position: absolute; left: 300px; top: 0; width: 549px; height: 900px;
    background:
      radial-gradient(ellipse 180px 260px at 70% 25%, rgba(244,148,35,.35), transparent 70%),
      radial-gradient(ellipse 220px 300px at 40% 45%, rgba(230,110,90,.22), transparent 70%),
      radial-gradient(ellipse 160px 220px at 85% 60%, rgba(120,130,200,.18), transparent 70%); }
  .shapes { position: absolute; inset: 0; }
  .theme-banner { position: absolute; left: 2px; top: 50px; width: 395px; height: 156px;
    background: var(--orange); display: flex; align-items: center; justify-content: center; }
  .theme-banner p { color: var(--white); font-style: italic; font-weight: 500; font-size: 33px; }
  .event-title { position: absolute; left: 425px; top: 58px; color: var(--navy);
    font-weight: 700; font-size: 52px; line-height: 51px; letter-spacing: -.5px; }
  .focus-words { position: absolute; left: 431px; top: 232px; font-weight: 700; font-size: 18px; color: var(--ink); }
  .schedule { position: absolute; left: 420px; top: 426px; display: flex; }
  .day { text-align: center; padding: 0 4px; }
  .day + .day { border-left: 1.5px solid var(--ink); }
  .day-month { font-weight: 600; font-size: 31px; line-height: 36px; color: var(--ink); }
  .day-date { font-weight: 700; font-size: 86px; line-height: 80px; color: var(--navy); letter-spacing: -2px; }
  .day-time { font-weight: 700; font-size: 15px; line-height: 30px; color: var(--ink); }
  .day:nth-child(1) { width: 120px; }
  .day:nth-child(2) { width: 146px; }
  .day:nth-child(3) { width: 126px; }
  .venue { position: absolute; left: 425px; top: 618px; font-size: 16.5px; line-height: 24px; color: var(--ink); }
  .contact { position: absolute; left: 426px; top: 808px; font-size: 16.5px; line-height: 24px; color: var(--ink); }
  .contact h2 { font-size: 16.5px; font-weight: 600; }
  .speaker-name { position: absolute; left: 42px; top: 1117px; font-weight: 600; font-size: 31px; color: var(--white); }
  .brand-name { position: absolute; left: 590px; top: 1068px; font-weight: 400; font-size: 52px;
    letter-spacing: 1px; color: var(--white); }
</style>
</head>
<body>
  <main class="flyer">
    <div class="flame-backdrop" role="img" aria-label="Soft flame texture background"></div>

    <svg class="shapes" width="849" height="1200" viewBox="0 0 849 1200">
      <defs>
        <linearGradient id="speakerTone" x1="0" y1="0" x2="0" y2="1">
          <stop offset="0" stop-color="#c9a58f"/>
          <stop offset=".45" stop-color="#e0644a"/>
          <stop offset="1" stop-color="#c8503c"/>
        </linearGradient>
      </defs>
      <polygon class="speaker-photo" role="img" aria-label="Portrait photo of the speaker, Prophet Marcus Olunde, in a coral jacket"
        points="0,330 120,250 250,222 360,300 390,600 405,1050 0,943" fill="url(#speakerTone)"/>
      <polygon class="accent-band" points="400,1049 849,928 849,988 424,1056" fill="var(--orange)"/>
      <polygon class="footer-band" points="0,943 424,1056 849,986 849,1200 0,1200" fill="var(--navy)"/>
    </svg>

    <div class="theme-banner"><p>In Fire and On Fire</p></div>

    <h1 class="event-title">KESTREL<br>SUMMIT<br>2020</h1>
    <p class="focus-words">FIRE, REVIVAL, PROPHETIC</p>

    <section class="schedule">
      <div class="day">
        <div class="day-month">DEC</div>
        <div class="day-date">31</div>
        <div class="day-time">@ 6:30 pm</div>
      </div>
      <div class="day">
        <div class="day-month">JAN</div>
        <div class="day-date">1,2</div>
        <div class="day-time">@ 6:30 pm</div>
      </div>
      <div class="day">
        <div class="day-month">JAN</div>
        <div class="day-date">3</div>
        <div class="day-time">@ 4:30 pm</div>
      </div>
    </section>

    <address class="venue" style="font-style:normal">
      Harlow Community Center,<br>239 Fennimore Street, Portland, ME 04117
    </address>

    <section class="contact">
      <h2>Contact information</h2>
      <p>contact@brightmeadowfold.org</p>
      <p>Telephone number: 207 583 2914</p>
    </section>

    <p class="speaker-name">Prophet Marcus Olunde</p>
    <p class="brand-name">VESPRA</p>
  </main>
</body>
</html>
```